Leafline Nutrition

we provide nutritional consulting for loss weight and changing food habits. The clinic is promoting the life healthy, as well as natural and balanced diets that help in the control weight and for the treatment to diseases.

Reason: Waiting some desings.

Reason: Waiting some designers

Reason: Waiting for changes.

Target Market(s)

Mostly women and men aged 30-55, both with overweight, obesity and problems with your food habits.

Industry/Entity Type

Weight

Font styles to use
Script

Colors
cadf82
ffc214
b868aa
f68d4d
0393ce
33b7a4
acd037
cbdf83
eaf2cf

Requirements
Must have
• lively and natural colors
logo that evokes healthy weight, concept of healthy natural food
Nice to have
• Slim fit image with a elegant and simple design
Should not have
• Preferably not used photograps, old-Style, Boring colors

```html
<!DOCTYPE html>
<html lang="en">
<head>
<meta charset="utf-8">
<title>Leafline Nutrition – Business Card</title>
<link href="https://fonts.googleapis.com/css2?family=Exo+2:wght@500;600;700&display=swap" rel="stylesheet">
<style>
  :root {
    --backdrop: #e9ebee;
    --card-white: #ffffff;
    --brand-blue: #0393ce;
    --blue-deep: #0a7fc0;
    --blue-light: #2eaae6;
    --leaf-green: #acd037;
    --leaf-pale: #cbdf83;
    --text-light: #ffffff;
  }
  * { margin: 0; padding: 0; box-sizing: border-box; }
  html, body {
    width: 1200px; height: 901px; overflow: hidden;
    background: var(--backdrop);
  }
  .canvas { position: relative; width: 1200px; height: 901px; }
  .business-card {
    position: absolute; left: 100px; top: 165px;
    width: 1000px; height: 571px;
    border-radius: 48px; overflow: hidden;
    background: var(--card-white);
    box-shadow: 0 10px 30px rgba(0,0,0,0.12);
  }
  .wave-field {
    position: absolute; left: 0; right: 0; top: 250px; bottom: 0;
    background: linear-gradient(180deg,
      var(--leaf-green) 0%, var(--leaf-pale) 7%,
      var(--blue-light) 14%, var(--brand-blue) 55%, var(--blue-deep) 100%);
  }
  .brand {
    position: absolute; left: 110px; top: 120px;
    display: flex; align-items: center; gap: 16px;
  }
  .brand-dot {
    width: 44px; height: 44px; border-radius: 50%;
    background: var(--leaf-green);
  }
  .brand-name {
    font-family: "Exo 2", sans-serif; font-weight: 500;
    font-size: 38px; color: var(--brand-blue);
  }
  .holder {
    position: absolute; left: 46px; top: 330px;
    color: var(--text-light); font-family: "Exo 2", sans-serif;
  }
  .holder-name { font-size: 36px; font-weight: 700; letter-spacing: 2px; line-height: 1.1; }
  .holder-role { font-size: 15px; font-weight: 600; letter-spacing: 1.5px; margin-top: 4px; }
  .contact {
    position: absolute; right: 48px; top: 300px;
    color: var(--text-light); font-family: "Exo 2", sans-serif;
    text-align: right; font-weight: 600;
  }
  .contact-address { font-size: 18px; line-height: 25px; margin-bottom: 18px; }
  .contact-line {
    display: flex; justify-content: flex-end; align-items: center; gap: 10px;
    font-size: 15px; height: 28px;
  }
  .contact-line svg { width: 16px; height: 16px; fill: var(--text-light); flex: none; }
</style>
</head>
<body>
<div class="canvas">
  <div class="business-card">
    <div class="wave-field" role="img" aria-label="Decorative blue wave field with green ribbon swooshes"></div>

    <div class="brand">
      <span class="brand-dot"></span>
      <span class="brand-name">Leafline Nutrition</span>
    </div>

    <div class="holder">
      <div class="holder-name">DANIEL MARSH</div>
      <div class="holder-role">MANAGING DIRECTOR</div>
    </div>

    <div class="contact">
      <div class="contact-address">27, 9th floor, Park Crescent<br>Road KLT</div>
      <div class="contact-line">014 552 7390
        <svg viewBox="0 0 16 16"><path d="M3 1l3 3-2 2c1 2 3 4 5 5l2-2 3 3-2 3C7 15 1 9 1 3z"/></svg>
      </div>
      <div class="contact-line">014 552 7390
        <svg viewBox="0 0 16 16"><path d="M4 0h8v16H4z M5.5 2v10h5V2z M7 13.5h2v1H7z" fill-rule="evenodd"/></svg>
      </div>
      <div class="contact-line">014 552 7390
        <svg viewBox="0 0 16 16"><path d="M1 6h14v9H1z M4 1h8v4H4z M3 8h2v2H3z M7 8h2v2H7z M11 8h2v2h-2z" fill-rule="evenodd"/></svg>
      </div>
      <div class="contact-line">hello@leaflinemail.com
        <svg viewBox="0 0 16 16"><path d="M1 3h14v10H1z M2 4l6 5 6-5" fill-rule="evenodd"/></svg>
      </div>
      <div class="contact-line">www.leaflinenutrition.com
        <svg viewBox="0 0 16 16"><circle cx="8" cy="8" r="7"/><path d="M1 8h14M8 1c-3 4-3 10 0 14M8 1c3 4 3 10 0 14" stroke="#0a7fc0" stroke-width="1.2" fill="none"/></svg>
      </div>
    </div>
  </div>
</div>
</body>
</html>
```